Website Design Needed for Fundmeadow-style Site

I need a design for a new website that is similar in concept in some ways to fundmeadow.example, but with a completely different market.

On one side, the site allows people to post projects for people to help fund, but where fundmeadow.example is focused on "creative" projects, this new site is focused on more serious "business-like" projects.

On the other side, the site allows visitors to help fund projects by pledging money in return for various rewards. In the attached image, ProjectDetailsConcept.png, the sidebar currently does not show the rewards mocked up, but there would need to be rewards listed there similar to what is shown here: http://www.fundmeadow.example/projects/torvel/paper-loop?ref=spotlight

The Project Details page will contain all the details for a given project. Note that some details are on different tabs on this page. Also note that the project description could be VERY long in some cases.

IMPORTANT: Although I have attached some concept images, please keep in mind that these are very rough and are mainly to illustrate what sort of content needs to be on the pages. None of the content on these mockup pages is final content.

Feel free to experiment with different layouts and concepts if you think they present the information better.

Pages Needed
1. Front Page - Shows main feature area, sub feature area, main menu, other links, search field and footer

2. Search/Browse Page - Lets users refine a search by clicking category names, locations, sort order, etc. Search results are listed below with next/prev controls and page number controls to navigate the results.

3. Project Details Page - Presents details of a given project. The specific details of the page content are not especially important. It is important that the Project Details Page allows multiple sections or tabs to be displayed though. The content in the sidebar of ProjectDetailsConcept.png is fairly representative of what might go there, especially in the top section of the sidebar. The top section should standout from the bottom section of the sidebar.

Keywords to try to relate in the site design: reliable, progressive, innovative, trustworthy, successful

Note that I do not yet have a logo for this site, but assume it is roughly the size and shape of the placeholder in the attached mockups.
Updates

I did some looking around at existing templates.

There are layout and color schemes in all of these that I like:

http://cms.layoutbarn.example/wordpress_41736/ (I quite like this one & it has dynamic)
http://38215.layouts.pagenook.example/
http://osc3.layoutbarn.example/stretched_27591/ (green with orange/yellow is nice)
http://images.osc3.layoutbarn.example/wt_35238/index.html

Also, please give consideration to the font choice for the site.  If necessary I can use cufon, Sifr or @fontface.

NOTE: I added another file called GreenHeaderMockup.png that is based on one of the website links in my previous update.

I like the body, but not the following aspects:

1. The header area needs some rework.  Maybe just a texture.

2. The project info for the featured project looks out of place.  Not sure where a better place would be, but see what comes to mind for you.

3. The project cards at the bottom are some variations...not sure which one I like the most.  Alternatives?

Feel free to ask questions.

Thanks.

Industry/Entity Type

Business

Requirements
Must have
• There must be a dynamic "Featured Projects" area near the top of the home page. This is similar in concept to the featured apps shown in the top of the Quillo Tool Bazaar. The set of available projects should somehow rotate or transition to focus on one project at a time while still leaving the others visible, but smaller. See the attached FrontPageConcept1.png image for a rough idea. Of course you are not responsible for coding the dynamic behavior, but you need to prepare the required graphical components to support any dynamic behavior you design.

The Search/Browse page must show a collection of "project cards", each of which contains some basic information about the project and an image. I have attached a file that shows some possible layouts for project cards.

See the attached SearchConcept1.png image for a concept that places all the search controls along the top, and the search results below. The concept shows two wide rows of project cards, but it would also be acceptable to show 4 rows of taller cards as in SearchConcept2.png

See the attached SearchConcept2.png image for a concept that places all the search controls in a sidebar, and the search results next to the sidebar. With this orientation, I think 3 tall project cards per row are all that can fit.

Should not have
• Must not use Flash or any other browser plugin.

```html
<!DOCTYPE html>
<html lang="en">
<head>
<meta charset="utf-8">
<title>Fundmeadow – Home</title>
<link rel="stylesheet" href="https://fonts.googleapis.com/css2?family=PT+Sans:wght@400;700&family=Tinos:wght@400;700&display=swap">
<style>
:root{
  --green-deep:#1f5d0a;
  --green-mid:#3f8f12;
  --green-bright:#7cc321;
  --green-lime:#a6dd3a;
  --green-pale:#c8ec7a;
  --ink:#222;
  --ink-soft:#555;
  --ink-faint:#888;
  --card-bg:#f3f3f3;
  --card-line:#dcdcdc;
  --page:#ffffff;
  --bar-dark:#1c1c1c;
}
*{box-sizing:border-box;margin:0;padding:0}
html,body{width:783px;height:1200px;overflow:hidden;background:var(--page)}
body{position:relative;font-family:"PT Sans",sans-serif;color:var(--ink)}

/* header */
.site-header{position:absolute;left:0;top:0;width:783px;height:83px;
  background:linear-gradient(100deg,#1d4d08 0%,#3d8a10 35%,#5fae1a 55%,#2f7a0c 75%,#1a4a06 100%)}
.logo{position:absolute;left:29px;top:28px;font-family:"Tinos",serif;font-weight:700;font-size:25px;color:#fff;letter-spacing:.3px}
.account-links{position:absolute;right:38px;top:20px;font-family:"Tinos",serif;font-size:11px;color:#d6ee7a}
.account-links span{margin:0 8px;color:#9fd04a}
.top-menu{position:absolute;left:504px;top:48px;font-family:"Tinos",serif;font-size:14px;color:#fff;display:flex;gap:22px}
.social-top{position:absolute;right:8px;top:47px;display:flex;gap:10px}
.social-chip{display:flex;align-items:center;gap:3px;font-family:"PT Sans",sans-serif;font-size:9px;color:#cfe98b;white-space:nowrap}
.social-chip i{display:block;width:9px;height:9px;background:#8fc63c}

/* nav */
.main-nav{position:absolute;left:0;top:83px;width:783px;height:34px;
  background:linear-gradient(#8fd12c,#5fae14);border-bottom:1px solid #3e7d0c}
.main-nav a{position:absolute;top:0;height:34px;line-height:34px;font-family:"Tinos",serif;font-size:14px;color:#fff;text-decoration:none}
.main-nav .active{left:31px;width:78px;text-align:center;background:linear-gradient(#3c8a10,#2c6c08)}
.search{position:absolute;left:551px;top:5px;width:200px;height:25px;background:#f2f2f2;border:1px solid #cfcfcf;border-radius:2px;font-size:10px;color:#666;padding:6px 9px}
.search svg{position:absolute;right:6px;top:4px}

/* hero */
.hero{position:absolute;left:31px;top:137px;width:552px;height:270px;border:3px solid #2a2a2a;border-bottom:none;
  background:radial-gradient(ellipse at 45% 40%,#e57d1f 0%,#c85e10 45%,#8c3b08 100%)}
.hero-photo{position:absolute;inset:0}
.hero-info{position:absolute;left:15px;top:101px;width:243px;height:103px;background:rgba(255,255,255,.28);border:1px solid rgba(255,255,255,.45);border-radius:4px;color:#fff;padding:9px 10px}
.hero-info h3{font-weight:400;font-size:14px}
.hero-info .loc{font-size:10px;margin-top:6px;display:flex;align-items:center;gap:4px}
.hero-info .funded{font-size:10px;margin-top:10px}
.hero-progress{position:relative;margin-top:6px;height:15px;background:#1a1a1a;border-radius:2px;font-size:10px;color:#fff}
.hero-progress b{position:absolute;left:0;top:0;height:15px;width:60%;background:linear-gradient(#a6e03c,#4e9a10);border-radius:2px;font-weight:400;color:#222;padding-left:6px;line-height:15px}
.hero-progress span{position:absolute;right:8px;line-height:15px}
.hero-caption{position:absolute;left:0;bottom:0;width:546px;height:51px;background:linear-gradient(#8fd12c,#4e9a0e);border-radius:8px 8px 0 0;color:#fff;padding:5px 14px}
.hero-caption h4{font-weight:400;font-size:13px;color:#f1ffd0}
.hero-caption p{font-size:9.5px;font-style:italic;line-height:12px;color:#223a05}
.thumbs{position:absolute;left:583px;top:137px;width:168px;height:270px}
.thumb{position:absolute;left:0;width:168px;border:3px solid #2a2a2a}
.thumb.current{border-color:var(--green-bright)}
.t1{top:0;height:90px;background:linear-gradient(135deg,#3d5a8a,#1e2a45)}
.t2{top:90px;height:90px;background:linear-gradient(135deg,#e8e8ee,#6a6070)}
.t3{top:180px;height:90px;background:linear-gradient(135deg,#8aa5bd,#3d5670)}

/* featured */
.section-title{position:absolute;left:0;top:429px;width:783px;text-align:center;font-size:24px;font-weight:400;color:#111}
.rule{position:absolute;left:29px;width:720px;border-top:1px dashed #bbb}

.card{position:absolute;width:327px;height:247px;background:linear-gradient(#f7f7f7,#ececec);border:1px solid var(--card-line);border-radius:4px;box-shadow:0 3px 5px rgba(0,0,0,.12)}
.card-tab{position:absolute;left:80px;top:-6px;width:168px;height:28px;background:linear-gradient(#b4e54e,#6fb81a);border-radius:2px;color:#fff;font-size:13px;text-align:center;line-height:28px;letter-spacing:.4px;text-shadow:0 1px 1px rgba(0,0,0,.25)}
.card-tab::before,.card-tab::after{content:"";position:absolute;top:0;border-bottom:6px solid #2c5e08}
.card-tab::before{left:-5px;border-left:5px solid transparent}
.card-tab::after{right:-5px;border-right:5px solid transparent}
.share{position:absolute;left:264px;top:9px;display:flex;gap:4px}
.share i{display:block;width:12px;height:12px;border-radius:2px}
.share .plus{background:#222;color:#fff;font-style:normal;font-size:11px;line-height:11px;text-align:center}
.share .s2{background:#5ab4e4}.share .s3{background:#3b5a98}
.card-divider{position:absolute;left:16px;top:34px;width:295px;border-top:1px solid #d8d8d8}
.card-photo{position:absolute;left:16px;top:47px;width:128px;height:111px;border:3px solid #fff;box-shadow:0 0 2px rgba(0,0,0,.3)}
.card h2{position:absolute;left:163px;top:42px;font-size:16px;font-weight:400;color:#111}
.card .blurb{position:absolute;left:163px;top:66px;width:150px;font-size:8.6px;line-height:11px;color:#777;text-align:justify}
.card .meta{position:absolute;left:16px;top:167px;font-size:10.5px;line-height:15px;color:#111}
.card .meta .loc{display:flex;align-items:center;gap:3px}
.bar{position:absolute;left:16px;top:215px;width:130px;height:11px;background:#1a1a1a;border-radius:2px}
.bar b{display:block;width:72px;height:11px;background:linear-gradient(#bdea55,#5ea811);border-radius:2px;font-weight:400;font-size:8px;line-height:11px;padding-left:7px;color:#222}

/* footer */
.footer-col{position:absolute;top:1046px}
.footer-col h5{font-size:13px;font-weight:400;color:#111;margin-bottom:8px}
.footer-col li{list-style:none;font-size:10.5px;line-height:15px;color:#666}
.cat-grid{display:grid;grid-template-columns:108px 108px 108px}
.newsletter p{font-size:9.5px;color:#555}
.newsletter .email{margin-top:7px;width:175px;height:24px;background:linear-gradient(#aaa,#ccc);border:1px solid #999;font-size:10px;color:#444;padding:6px 11px}
.newsletter .btn{margin:11px 0 0 60px;width:64px;height:22px;border:1px solid #aaa;border-radius:3px;background:linear-gradient(#fff,#ddd);font-size:9px;text-align:center;line-height:20px;color:#222}
.bottom-bar{position:absolute;left:0;top:1158px;width:783px;height:42px;background:linear-gradient(#f2f2f2,#dcdcdc);border-top:1px solid #ccc}
.copyright{position:absolute;left:29px;top:15px;font-size:9px;font-style:italic;color:#333}
.copyright a{color:#777;margin-left:10px;text-decoration:none}
.social-foot{position:absolute;right:31px;top:14px;display:flex;gap:8px}
.social-foot .social-chip{color:#444;font-size:9px}
.social-foot .social-chip i{width:10px;height:10px}
</style>
</head>
<body>

<header class="site-header">
  <div class="logo">LOGO GOES HERE</div>
  <div class="account-links">Register<span>|</span>Login</div>
  <nav class="top-menu"><span>Blog</span><span>FAQ</span><span>Company</span></nav>
  <div class="social-top">
    <span class="social-chip"><i></i>Friendly</span>
    <span class="social-chip"><i></i>Chirpline</span>
  </div>
</header>

<nav class="main-nav">
  <a class="active">Features</a>
  <a style="left:135px">Browse</a>
  <a style="left:221px">My Account</a>
  <a style="left:336px">Portfolio</a>
  <div class="search">Search
    <svg width="16" height="16" viewBox="0 0 16 16"><circle cx="6.5" cy="6.5" r="4.5" fill="none" stroke="#444" stroke-width="1.8"/><line x1="10" y1="10" x2="14.5" y2="14.5" stroke="#444" stroke-width="2.4"/></svg>
  </div>
</nav>

<section class="hero">
  <div class="hero-photo" role="img" aria-label="Featured project photo: a small robot toy on an orange table"></div>
  <div class="hero-info">
    <h3>John Smith &amp; Frank Johnson</h3>
    <div class="loc"><svg width="8" height="11" viewBox="0 0 8 11"><path d="M4 0a4 4 0 0 1 4 4c0 3-4 7-4 7S0 7 0 4a4 4 0 0 1 4-4z" fill="#fff"/><circle cx="4" cy="4" r="1.5" fill="#b05a18"/></svg>Vancouver, B.C, Canada</div>
    <div class="funded">Funded $65,000 of $100,000</div>
    <div class="hero-progress"><b>65%</b><span>8 days left</span></div>
  </div>
  <div class="hero-caption">
    <h4>Our Design Studio is a professional interactive agency</h4>
    <p>Lorem ipsum dolor sit amet, consectetur adipisicing elit, sed do eiusmod tempor incididunt ut labore et dolore magna aliqua. Ut enim ad minim veniam, quis nostrud exercitation ullamco laboris nisi ...</p>
  </div>
</section>
<div class="thumbs">
  <div class="thumb t1 current" role="img" aria-label="Project thumbnail: handheld game device"></div>
  <div class="thumb t2" role="img" aria-label="Project thumbnail: people at an event"></div>
  <div class="thumb t3" role="img" aria-label="Project thumbnail: blue interface diagram"></div>
</div>

<h1 class="section-title">Featured Projets of the day</h1>
<div class="rule" style="top:463px"></div>

<article class="card" style="left:40px;top:480px">
  <div class="card-tab">New &amp; Noteworthy</div>
  <div class="share"><i class="plus">+</i><i class="s2"></i><i class="s3"></i></div>
  <div class="card-divider"></div>
  <div class="card-photo" role="img" aria-label="Project photo: man riding a personal electric vehicle" style="background:linear-gradient(135deg,#c9c9b8,#5a5a48)"></div>
  <h2>Project Title Here</h2>
  <p class="blurb">Lorem ipsum dolor sit amet, consectetur adipisicing elit, sed do eiusmod tempor incididunt ut labore et dolore magna aliqua. Ut enim ad minim veniam, quis nostrud exercitation ullamco laboris nisi ut aliquip ex ea commodo consequat. Duis aute irure dolor in reprehenderit in voluptate velit esse cillum dolore eu fugiat nulla pariatur. Excepteur sint occaecat cupidatat non proident, sunt in culpa qui officia deserunt mollit anim id est</p>
  <div class="meta"><div class="loc"><svg width="8" height="11" viewBox="0 0 8 11"><path d="M4 0a4 4 0 0 1 4 4c0 3-4 7-4 7S0 7 0 4a4 4 0 0 1 4-4z" fill="#222"/><circle cx="4" cy="4" r="1.5" fill="#fff"/></svg>Vancouver, B.C, Canada</div>8 days left<br>Funded $65,000 of $100,000</div>
  <div class="bar"><b>65%</b></div>
</article>

<article class="card" style="left:416px;top:480px">
  <div class="card-tab">Popular</div>
  <div class="share"><i class="plus">+</i><i class="s2"></i><i class="s3"></i></div>
  <div class="card-divider"></div>
  <div class="card-photo" role="img" aria-label="Project artwork: cartoon animal sticker app cover" style="background:linear-gradient(135deg,#9ccf3a,#3f7f14)"></div>
  <h2>Project Title Here</h2>
  <p class="blurb">Lorem ipsum dolor sit amet, consectetur adipisicing elit, sed do eiusmod tempor incididunt ut labore et dolore magna aliqua. Ut enim ad minim veniam, quis nostrud exercitation ullamco laboris nisi ut aliquip ex ea commodo consequat. Duis aute irure dolor in reprehenderit in voluptate velit esse cillum dolore eu fugiat nulla pariatur. Excepteur sint occaecat cupidatat non proident, sunt in culpa qui officia deserunt mollit anim id est</p>
  <div class="meta"><div class="loc"><svg width="8" height="11" viewBox="0 0 8 11"><path d="M4 0a4 4 0 0 1 4 4c0 3-4 7-4 7S0 7 0 4a4 4 0 0 1 4-4z" fill="#222"/><circle cx="4" cy="4" r="1.5" fill="#fff"/></svg>Vancouver, B.C, Canada</div>8 days left<br>Funded $65,000 of $100,000</div>
  <div class="bar"><b>65%</b></div>
</article>

<article class="card" style="left:40px;top:764px">
  <div class="card-tab">Closing Soon</div>
  <div class="share"><i class="plus">+</i><i class="s2"></i><i class="s3"></i></div>
  <div class="card-divider"></div>
  <div class="card-photo" role="img" aria-label="Project photo: costumed statue figure in a hall" style="background:linear-gradient(135deg,#b9b2a6,#3a3632)"></div>
  <h2>Project Title Here</h2>
  <p class="blurb">Lorem ipsum dolor sit amet, consectetur adipisicing elit, sed do eiusmod tempor incididunt ut labore et dolore magna aliqua. Ut enim ad minim veniam, quis nostrud exercitation ullamco laboris nisi ut aliquip ex ea commodo consequat. Duis aute irure dolor in reprehenderit in voluptate velit esse cillum dolore eu fugiat nulla pariatur. Excepteur sint occaecat cupidatat non proident, sunt in culpa qui officia deserunt mollit anim id est</p>
  <div class="meta"><div class="loc"><svg width="8" height="11" viewBox="0 0 8 11"><path d="M4 0a4 4 0 0 1 4 4c0 3-4 7-4 7S0 7 0 4a4 4 0 0 1 4-4z" fill="#222"/><circle cx="4" cy="4" r="1.5" fill="#fff"/></svg>Vancouver, B.C, Canada</div>8 days left<br>Funded $65,000 of $100,000</div>
  <div class="bar"><b>65%</b></div>
</article>

<article class="card" style="left:416px;top:764px">
  <div class="card-tab">Nearly Funded</div>
  <div class="share"><i class="plus">+</i><i class="s2"></i><i class="s3"></i></div>
  <div class="card-divider"></div>
  <div class="card-photo" role="img" aria-label="Project photo: hand sketching a flow chart" style="background:linear-gradient(135deg,#f4f0ec,#b99a82)"></div>
  <h2>Project Title Here</h2>
  <p class="blurb">Lorem ipsum dolor sit amet, consectetur adipisicing elit, sed do eiusmod tempor incididunt ut labore et dolore magna aliqua. Ut enim ad minim veniam, quis nostrud exercitation ullamco laboris nisi ut aliquip ex ea commodo consequat. Duis aute irure dolor in reprehenderit in voluptate velit esse cillum dolore eu fugiat nulla pariatur. Excepteur sint occaecat cupidatat non proident, sunt in culpa qui officia deserunt mollit anim id est</p>
  <div class="meta"><div class="loc"><svg width="8" height="11" viewBox="0 0 8 11"><path d="M4 0a4 4 0 0 1 4 4c0 3-4 7-4 7S0 7 0 4a4 4 0 0 1 4-4z" fill="#222"/><circle cx="4" cy="4" r="1.5" fill="#fff"/></svg>Vancouver, B.C, Canada</div>8 days left<br>Funded $65,000 of $100,000</div>
  <div class="bar"><b>65%</b></div>
</article>

<div class="rule" style="top:1035px"></div>

<footer>
  <div class="footer-col" style="left:30px">
    <h5>Common Links</h5>
    <ul><li>My Account</li><li>Blog</li><li>Company</li><li>FAQ</li></ul>
  </div>
  <div class="footer-col" style="left:198px">
    <h5>Categories</h5>
    <ul class="cat-grid">
      <li>Category 1 name</li><li>Category 5 name</li><li>Category 9 name</li>
      <li>Category 2 name</li><li>Category 6 name</li><li>Category 10 name</li>
      <li>Category 3 name</li><li>Category 7 name</li><li>Category 11 name</li>
      <li>Category 4 name</li><li>Category 8 name</li><li>Category 12 name</li>
    </ul>
  </div>
  <div class="footer-col newsletter" style="left:553px">
    <h5 style="margin-bottom:4px">Newsletter</h5>
    <p>Subscribe to our newsletter for updates</p>
    <div class="email">Your email</div>
    <div class="btn">Subscribe</div>
  </div>

  <div class="bottom-bar">
    <div class="copyright">Copyright 2011 Company INC. <a>Terms of Use</a><a>Privacy Policy</a><a>Contact Us</a></div>
    <div class="social-foot">
      <span class="social-chip"><i style="background:#c4302b"></i>Vidstream</span>
      <span class="social-chip"><i style="background:#1ab7ea"></i>Clipnest</span>
      <span class="social-chip"><i style="background:#3b5998"></i>Friendly</span>
      <span class="social-chip"><i style="background:#f58a1f"></i>Feed</span>
      <span class="social-chip"><i style="background:#5fc3ef"></i>Chirpline</span>
    </div>
  </div>
</footer>

</body>
</html>
```